Poly Gel bottle Design that stands out for Nail Company

I need a label design for the poly gel polish bottle. We are looking for a design that fit our brand store color and a clean design similar to our competitor.

We have 3 bottle Title: Gel Top Coat, Gel base Coat, Gel Matte Coat
The bottle will be white.

Also I will need 1 label for the extension gel.

Bottle volume is 15ml/0.5 fl oz

Target Market(s)

beauty acrylic nail and poly gel nail

Industry/Entity Type

Nail

Font styles to use
Serif
Decorative

Colors
6c459b

Requirements
Must have
• store color scheme. www.tealpebbleshop.com

```html
<!DOCTYPE html>
<html lang="en">
<head>
<meta charset="utf-8">
<title>Teal Pebble – Poly Gel Labels</title>
<link rel="stylesheet" href="https://fonts.googleapis.com/css2?family=Old+Standard+TT:wght@400;700&family=Great+Vibes&family=Josefin+Sans:wght@400&display=swap">
<style>
  :root {
    --backdrop: #808080;
    --label: #f7f8f3;
    --label-edge: #e6e8df;
    --ink: #0a0a0a;
    --accent-top: #f2c4d4;
    --accent-matte: #c6b4dc;
    --accent-base: #ead6a2;
  }
  * { margin: 0; padding: 0; box-sizing: border-box; }
  html, body {
    width: 1200px;
    height: 886px;
    overflow: hidden;
    background: var(--backdrop);
  }
  .canvas {
    position: relative;
    width: 1200px;
    height: 886px;
    background: var(--backdrop);
  }
  .label {
    position: absolute;
    top: 380px;
    width: 270px;
    height: 345px;
    background: linear-gradient(90deg, var(--label-edge) 0%, var(--label) 12%, var(--label) 88%, var(--label-edge) 100%);
    border-radius: 22px;
    text-align: center;
    color: var(--ink);
  }
  .label--top   { left: 143px; --accent: var(--accent-top); }
  .label--matte { left: 476px; --accent: var(--accent-matte); }
  .label--base  { left: 802px; --accent: var(--accent-base); }

  .label__flourish {
    position: absolute;
    left: 15px;
    top: 100px;
    width: 240px;
    height: 130px;
    border-radius: 50%;
    background: radial-gradient(ellipse at center, var(--accent) 0%, transparent 70%);
    opacity: 0.55;
  }
  .label__brand {
    position: absolute;
    top: 58px;
    left: 0;
    width: 100%;
    font-family: "Old Standard TT", serif;
    font-weight: 700;
    font-size: 34px;
    letter-spacing: 0.5px;
  }
  .label__title {
    position: absolute;
    top: 147px;
    left: 0;
    width: 100%;
    font-family: "Old Standard TT", serif;
    font-weight: 400;
    font-size: 26px;
    line-height: 29px;
  }
  .label__type {
    position: absolute;
    top: 228px;
    left: 0;
    width: 100%;
    font-family: "Great Vibes", cursive;
    font-size: 32px;
  }
  .label__volume {
    position: absolute;
    top: 281px;
    left: 0;
    width: 100%;
    font-family: "Josefin Sans", sans-serif;
    font-size: 13px;
  }
</style>
</head>
<body>
<main class="canvas">
  <section class="label label--top">
    <div class="label__flourish" role="img" aria-label="Soft pink calligraphic flourish ornament"></div>
    <p class="label__brand">teal pebble</p>
    <h2 class="label__title">GEL TOP<br>COAT</h2>
    <p class="label__type">poly gel polish</p>
    <p class="label__volume">15ml/0.5 fl oz</p>
  </section>

  <section class="label label--matte">
    <div class="label__flourish" role="img" aria-label="Soft lavender calligraphic flourish ornament"></div>
    <p class="label__brand">teal pebble</p>
    <h2 class="label__title">GEL MATTE<br>COAT</h2>
    <p class="label__type">poly gel polish</p>
    <p class="label__volume">15ml/0.5 fl oz</p>
  </section>

  <section class="label label--base">
    <div class="label__flourish" role="img" aria-label="Soft gold calligraphic flourish ornament"></div>
    <p class="label__brand">teal pebble</p>
    <h2 class="label__title">GEL BASE<br>COAT</h2>
    <p class="label__type">poly gel polish</p>
    <p class="label__volume">15ml/0.5 fl oz</p>
  </section>
</main>
</body>
</html>
```